Construction Company

Design a clutter free business card, it can be double-sided utilizing the logo for BDN Ltd simple with all relevant contact information.

Please also a letterhead design to function for the purposes of invoicing, all mail requirements, with header to be distinctive while the footer ties page together and incorporates all necessary information.

For now, please use generic / dummy text and when a winner is selected, I will disclose the contact information.

Hi Designers! Please read the updated brief which includes the design of a business card and letterhead. Thank you!

```html
<!DOCTYPE html>
<html lang="en">
<head>
<meta charset="utf-8">
<title>BDN Ltd – Business Card</title>
<link rel="stylesheet" href="https://fonts.googleapis.com/css2?family=Montserrat:wght@400;700&display=swap">
<style>
  :root {
    --navy: #1f3a80;
    --cream: #f9f9f1;
    --gold: #b89357;
    --gold-mark: #b8952a;
    --white: #ffffff;
    --paper: #ffffff;
    --sky: #93d3ea;
  }
  * { margin: 0; padding: 0; box-sizing: border-box; }
  html, body {
    width: 1200px;
    height: 2400px;
    overflow: hidden;
    background: var(--paper);
    font-family: "Montserrat", Arial, sans-serif;
  }
  .board { position: relative; width: 1200px; height: 2400px; }
  .board__sky {
    position: absolute;
    left: 0; top: 1200px;
    width: 1200px; height: 1200px;
    background: var(--sky);
  }
  .card {
    position: absolute;
    left: 300px;
    width: 600px;
    height: 343px;
    box-shadow: 4px 6px 8px rgba(0,0,0,0.22);
  }
  .card--front { background: var(--cream); }
  .card--back { background: var(--navy); color: var(--white); }

  .brand {
    position: absolute;
    left: 0; right: 0; top: 0; bottom: 0;
    display: flex;
    align-items: center;
    justify-content: center;
    gap: 18px;
  }
  .brand__dot {
    width: 34px; height: 34px;
    border-radius: 50%;
    background: var(--gold-mark);
  }
  .brand__name {
    font-weight: 700;
    font-size: 84px;
    letter-spacing: 0.01em;
    color: var(--navy);
    line-height: 1;
  }

  .person { position: absolute; left: 61px; top: 56px; }
  .person__name {
    font-weight: 700;
    font-size: 40px;
    line-height: 1;
    letter-spacing: 0.01em;
  }
  .person__role {
    margin-top: 8px;
    font-weight: 400;
    font-size: 16px;
    letter-spacing: 0.2em;
    color: var(--gold);
  }
  .contact {
    position: absolute;
    left: 170px;
    top: 214px;
    display: grid;
    grid-template-columns: 89px auto;
    column-gap: 11px;
    row-gap: 5px;
    font-size: 16px;
    line-height: 18px;
  }
  .contact__label {
    text-align: right;
    font-weight: 400;
    letter-spacing: 0.15em;
    color: var(--gold);
  }
  .contact__value {
    font-weight: 700;
    letter-spacing: 0.15em;
    color: var(--white);
  }
</style>
</head>
<body>
<main class="board">
  <section class="card card--front" style="top:200px">
    <div class="brand"><span class="brand__dot"></span><span class="brand__name">BDN Ltd</span></div>
  </section>
  <section class="card card--back" style="top:657px">
    <div class="person">
      <p class="person__name">John Doe</p>
      <p class="person__role">FOUNDER</p>
    </div>
    <div class="contact">
      <span class="contact__label">PHONE</span><span class="contact__value">+00 123 456 789</span>
      <span class="contact__label">E-MAIL</span><span class="contact__value">JohnDoe@BDNLTD.com</span>
      <span class="contact__label">WEB</span><span class="contact__value">www.BDNLTD.com</span>
    </div>
  </section>

  <div class="board__sky"></div>
  <section class="card card--back" style="top:1397px">
    <div class="person">
      <p class="person__name">John Doe</p>
      <p class="person__role">FOUNDER</p>
    </div>
    <div class="contact">
      <span class="contact__label">PHONE</span><span class="contact__value">+00 123 456 789</span>
      <span class="contact__label">E-MAIL</span><span class="contact__value">JohnDoe@BDNLTD.com</span>
      <span class="contact__label">WEB</span><span class="contact__value">www.BDNLTD.com</span>
    </div>
  </section>
  <section class="card card--front" style="top:1860px">
    <div class="brand"><span class="brand__dot"></span><span class="brand__name">BDN Ltd</span></div>
  </section>
</main>
</body>
</html>
```